Poster Design Project

I want word type poster for one place in london that will describe with words.I have attach one mine photo and two relevant text that will describe my city tybe project for the city of london at Fenwold Park.I want something like the eco-typography that I have attach.

Target Market(s)

my audience are adults 20-60

```html
<!DOCTYPE html>
<html lang="en">
<head>
<meta charset="utf-8">
<title>Fenwold Park — Poster</title>
<link rel="stylesheet" href="https://fonts.googleapis.com/css2?family=Cinzel:wght@500&family=Kalam:wght@700&family=Cabin+Condensed:wght@500&family=Crimson+Text:ital@1&display=swap">
<style>
  :root {
    --paper: #f7f2e2;
    --paper-glow: #fbf3c4;
    --gold: #e8bf5c;
    --gold-deep: #d9a640;
    --gold-soft: rgba(240, 210, 110, 0.55);
    --highlight: rgba(246, 226, 120, 0.85);
    --title-red: #d01a1a;
    --ink: #1a1714;
    --accent-red: #c8201c;
  }
  html, body {
    margin: 0;
    padding: 0;
    overflow: hidden;
    background: var(--paper);
  }
  .poster {
    position: relative;
    width: 849px;
    height: 1200px;
    overflow: hidden;
    background:
      radial-gradient(ellipse 420px 360px at 330px 560px, var(--paper-glow) 0%, rgba(251,243,196,0) 100%),
      radial-gradient(ellipse 300px 500px at 780px 300px, rgba(248,230,150,0.5) 0%, rgba(248,230,150,0) 100%),
      var(--paper);
  }

  /* Gold ornamental frame areas */
  .frame-ornament {
    position: absolute;
    border-radius: 60px;
  }
  .frame-ornament--top {
    left: 0; top: 0; width: 849px; height: 80px;
    background: linear-gradient(180deg, var(--gold) 0%, rgba(232,191,92,0) 100%);
  }
  .frame-ornament--top-left {
    left: 0; top: 40px; width: 200px; height: 340px;
    border-radius: 0 160px 160px 0;
    background: radial-gradient(ellipse at 30% 50%, var(--gold-soft) 0%, rgba(232,191,92,0) 72%);
  }
  .frame-ornament--left {
    left: 0; top: 0; width: 70px; height: 1200px;
    border-radius: 0;
    background: linear-gradient(90deg, var(--gold) 0%, rgba(232,191,92,0) 100%);
  }
  .frame-ornament--right {
    right: 0; top: 0; width: 70px; height: 1200px;
    border-radius: 0;
    background: linear-gradient(270deg, var(--gold) 0%, rgba(232,191,92,0) 100%);
  }
  .frame-ornament--bottom {
    left: 0; bottom: 0; width: 849px; height: 90px;
    border-radius: 0;
    background: linear-gradient(0deg, var(--gold) 0%, rgba(232,191,92,0) 100%);
  }
  .frame-ornament--bottom-right {
    right: 0; bottom: 0; width: 230px; height: 480px;
    border-radius: 200px 0 0 0;
    background: radial-gradient(ellipse at 70% 60%, var(--gold-soft) 0%, rgba(232,191,92,0) 72%);
  }

  .title {
    position: absolute;
    left: 0; top: 142px;
    width: 849px;
    margin: 0;
    text-align: center;
    font-family: "Cinzel", "Times New Roman", serif;
    font-weight: 500;
    font-size: 98px;
    line-height: 1;
    letter-spacing: 1px;
    color: var(--title-red);
    text-shadow: 2px 3px 3px rgba(120, 60, 0, 0.35);
    transform: scaleY(1.12);
  }

  .intro {
    position: absolute;
    left: 234px; top: 284px;
    width: 530px;
    margin: 0;
    font-family: "Kalam", "Comic Sans MS", cursive;
    font-weight: 700;
    font-size: 18px;
    line-height: 27px;
    color: var(--ink);
    transform: rotate(-3deg);
    transform-origin: left top;
  }

  .highlight {
    position: absolute;
    border-radius: 40px;
    background: radial-gradient(ellipse at center, var(--highlight) 40%, rgba(246,226,120,0) 72%);
  }
  .highlight--habitat { left: 80px; top: 440px; width: 480px; height: 200px; }
  .highlight--songbirds { left: 10px; top: 880px; width: 690px; height: 200px; }

  .fact {
    position: absolute;
    margin: 0;
    font-family: "Cabin Condensed", "Arial Narrow", sans-serif;
    font-weight: 500;
    color: var(--ink);
    transform-origin: left top;
  }
  .fact--habitat {
    left: 124px; top: 460px;
    width: 400px;
    font-size: 27px;
    line-height: 36px;
    text-align: center;
    transform: rotate(4deg);
  }
  .fact--lake {
    left: 110px; top: 760px;
    width: 600px;
    font-size: 27px;
    line-height: 38px;
    transform: rotate(-2.5deg);
  }
  .fact--songbirds {
    left: 52px; top: 942px;
    width: 640px;
    font-size: 34px;
    line-height: 46px;
    text-align: center;
    transform: rotate(-4deg);
  }

  .park-photo {
    position: absolute;
    left: 524px; top: 440px;
    width: 298px; height: 296px;
    border-radius: 18px 26px 14px 22px;
    background:
      linear-gradient(180deg, #3f7fd6 0%, #7aa8e0 38%, #a1785a 58%, #8a6a4a 78%, #c9a06a 100%);
    box-shadow: 0 0 12px 6px rgba(247, 242, 226, 0.9) inset;
  }

  .visitors {
    position: absolute;
    left: 700px; top: 1000px;
    width: 220px;
    margin: 0;
    font-family: "Crimson Text", Georgia, serif;
    font-style: italic;
    font-size: 19px;
    line-height: 22px;
    text-align: center;
    color: var(--accent-red);
    transform: rotate(70deg);
    transform-origin: center;
  }
</style>
</head>
<body>
  <main class="poster">
    <div class="frame-ornament frame-ornament--top" role="img" aria-label="Gold swirl ornament border along the top"></div>
    <div class="frame-ornament frame-ornament--left" role="img" aria-label="Gold swirl ornament border along the left edge"></div>
    <div class="frame-ornament frame-ornament--right" role="img" aria-label="Gold swirl ornament border along the right edge"></div>
    <div class="frame-ornament frame-ornament--bottom" role="img" aria-label="Gold swirl ornament border along the bottom"></div>
    <div class="frame-ornament frame-ornament--top-left" role="img" aria-label="Large gold spiral ornament"></div>
    <div class="frame-ornament frame-ornament--bottom-right" role="img" aria-label="Large gold spiral ornament"></div>

    <h1 class="title">FENWOLD PARK</h1>

    <p class="intro">Fenwold Park was created to satisfy a royal passion for hunting. But over the years it became a place where people have pursued many other pleasures.</p>

    <div class="highlight highlight--habitat"></div>
    <p class="fact fact--habitat">Fenwold Park provides a unique habitat in the heart of London for a diverse variety of species of flora and fauna.</p>

    <div class="park-photo" role="img" aria-label="Photo of gulls flying over bare trees and benches in the park under a blue sky"></div>

    <p class="fact fact--lake">The lake also attracts a large number of insects<br>that provides a perfect feeding ground for bats.</p>

    <div class="highlight highlight--songbirds"></div>
    <p class="fact fact--songbirds">The trees, shrub beds and herbaceous plantings provide tich habitats for song birds.</p>

    <p class="visitors">Over 7 million visitors<br>each year!</p>
  </main>
</body>
</html>
```